Web Design Project - Investor Services

I would like a simple and elegant web design for my company "Corvalo Management". The company will provide services to Corporate and Institutional investors for their needs with local/foreign investment vehicles. The website will have four pages to start: home, about us, services, contact.
I already chose a logo, and I will attach the source file. The color that I will most probably use for the logo will be blue, and i also like grey with a white background. For the website I would like to see light colors, maybe light green or grey, with the logo either in blue, grey or white (depeding on the background).
Target Market(s)
Investment managers and tax/legal advisors from top firms. This is the reason why I want something simple and elegant.
Industry/Entity Type
Investment
Requirements
Nice to have
- I do not want many pictures in the website, but I might include a couple of pictures of Madrid and maybe a picture of myself in the about us page (still deciding). I will attach some pictures of Madrid that I like, but feel free to search for others - i have others but i am not able to attach all of them.

```html
<!DOCTYPE html>
<html lang="en">
<head>
<meta charset="utf-8">
<title>Corvalo Management</title>
<link rel="stylesheet" href="https://fonts.googleapis.com/css2?family=Noto+Sans:wght@400;500&display=swap">
<style>
  :root {
    --brand-blue: #1f2a86;
    --navy: #0b0f57;
    --text: #555555;
    --heading: #111111;
    --rule: #c4c4c4;
    --footer-bg: #efefef;
    --white: #ffffff;
  }
  * { margin: 0; padding: 0; box-sizing: border-box; }
  html, body { width: 1200px; height: 1000px; overflow: hidden; background: var(--white); }
  body { position: relative; font-family: "Noto Sans", Verdana, sans-serif; color: var(--text); }

  .brand {
    position: absolute; left: 230px; top: 68px; width: 232px;
    font-size: 20px; font-weight: 400; color: var(--brand-blue);
    line-height: 26px; white-space: nowrap;
  }

  .main-nav {
    position: absolute; left: 467px; top: 63px; width: 506px; height: 37px;
    background: linear-gradient(#ffffff 0%, #f0f0f0 45%, #cfcfcf 100%);
    border-radius: 0 0 4px 4px;
    box-shadow: 0 4px 5px rgba(0,0,0,0.18);
    display: flex;
  }
  .main-nav a {
    height: 100%; display: flex; align-items: center; justify-content: center;
    font-size: 13px; color: var(--heading); text-decoration: none;
    border-right: 1px solid #8a8a8a;
  }
  .main-nav a:last-child { border-right: none; }
  .main-nav .home { width: 126px; padding-left: 30px; }
  .main-nav .about { width: 114px; }
  .main-nav .services { width: 108px; }
  .main-nav .contact { width: 158px; padding-right: 32px; }

  .hero {
    position: absolute; left: 228px; top: 124px; width: 747px; height: 281px;
    border-radius: 4px 4px 0 0;
    background: linear-gradient(180deg, #f7f7f9 0%, #eeeff3 35%, #c9cdd8 60%, #a9ab9f 80%, #8d8e80 100%);
  }
  .hero-shadow {
    position: absolute; left: 238px; top: 404px; width: 727px; height: 14px;
    background: radial-gradient(ellipse at top, rgba(0,0,0,0.22), rgba(0,0,0,0) 70%);
  }

  .column { position: absolute; top: 436px; width: 218px; }
  .column h2 {
    font-size: 15px; font-weight: 400; color: var(--heading);
    text-align: center; line-height: 20px; padding-bottom: 2px;
    border-bottom: 2px solid var(--rule);
  }
  .column .body { margin-top: 16px; font-size: 12.6px; line-height: 15px; letter-spacing: 0.35px; }
  .column p + p { margin-top: 15px; }
  .about { left: 230px; width: 228px; }
  .about h2 { width: 218px; padding-right: 30px; }
  .services { left: 488px; }
  .services h2 { padding-left: 15px; }
  .services ul { list-style: none; padding-left: 2px; }
  .services li { position: relative; }
  .services li + li { margin-top: 15px; }
  .services li::before {
    content: ""; position: absolute; left: -11px; top: 5px;
    width: 5px; height: 5px; border-radius: 50%; background: #111;
  }
  .testimonials { left: 745px; width: 222px; }
  .testimonials h2 { width: 218px; padding-left: 35px; }
  .testimonials .body { padding-left: 2px; }

  .btn {
    position: absolute; top: 757px; width: 99px; height: 23px;
    background: var(--navy); color: var(--white);
    font-size: 12px; line-height: 23px; text-align: center; text-decoration: none;
  }
  .btn-about { left: 342px; }
  .btn-services { left: 604px; }
  .btn-testimonials { left: 862px; }

  .site-footer {
    position: absolute; left: 0; top: 791px; width: 1200px; height: 209px;
    background: var(--footer-bg); border-top: 5px solid var(--navy);
  }
  .social { position: absolute; top: 9px; left: 860px; display: flex; gap: 26px; }
  .social span { width: 16px; height: 16px; border-radius: 50%; background: #111; display: block; }
  .footer-nav {
    position: absolute; top: 76px; left: 421px; display: flex;
    font-size: 11px; color: var(--heading);
  }
  .footer-nav a { color: var(--heading); text-decoration: none; }
  .footer-nav .f-home { width: 78px; }
  .footer-nav .f-about { width: 94px; }
  .footer-nav .f-services { width: 91px; }
  .copyright {
    position: absolute; top: 150px; left: 0; width: 1154px; text-align: center;
    font-size: 10px; color: var(--heading);
  }
</style>
</head>
<body>
  <header>
    <div class="brand">Corvalo Management</div>
    <nav class="main-nav">
      <a class="home" href="#">Home</a>
      <a class="about" href="#">About us</a>
      <a class="services" href="#">Services</a>
      <a class="contact" href="#">Contact us</a>
    </nav>
  </header>

  <div class="hero" role="img" aria-label="Photograph of the Madrid skyline with its business towers above the city"></div>
  <div class="hero-shadow"></div>

  <section class="column about">
    <h2>About us</h2>
    <div class="body">
      <p>Lorem ipsum dolor sit amet, consectetur adipisicing elit, sed do eiusmod tempor incididunt ut labore et dolore magna aliqua. Ut enim ad minim veniam, quis nostrud exercitation ullamco laboris nisi ut aliquip ex ea commodo consequat. Duis aute irure dolor in reprehenderit in voluptate velit esse cillum dolore eu fugiat nulla pariatur. Excepteur sint occaecat cupidatat non proident, sunt in culpa qui officia deserunt mollit anim id est laborum.</p>
    </div>
  </section>

  <section class="column services">
    <h2>Our Services</h2>
    <ul class="body">
      <li>Lorem ipsum dolor sit amet, consectetur adipisicing elit, sed do eiusmod tempor incididunt ut labore et dolore magna aliqua.</li>
      <li>Lorem ipsum dolor sit amet, consectetur adipisicing elit, sed do eiusmod tempor incididunt ut labore et dolore magna aliqua.</li>
      <li>Lorem ipsum dolor sit amet, consectetur adipisicing elit, sed do eiusmod tempor incididunt ut labore et dolore magna aliqua.</li>
      <li>Lorem ipsum dolor sit amet, consectetur adipisicing elit, labore et dolore magna aliqua.</li>
    </ul>
  </section>

  <section class="column testimonials">
    <h2>Testimonials</h2>
    <div class="body">
      <p>“Lorem ipsum dolor sit amet, consectetur adipisicing elit, sed do eiusmod tempor incididunt ut labore et dolore magna aliqua.”</p>
      <p>Lorem ipsum dolor sit amet, consectetur adipisicing elit, sed do eiusmod tempor incididunt ut labore et dolore magna aliqua.”</p>
      <p>Lorem ipsum dolor sit amet, consectetur adipisicing elit, sed do eiusmod tempor incididunt ut labore et dolore magna aliqua.”</p>
    </div>
  </section>

  <a class="btn btn-about" href="#">Learn more</a>
  <a class="btn btn-services" href="#">Learn more</a>
  <a class="btn btn-testimonials" href="#">Learn more</a>

  <footer class="site-footer">
    <div class="social">
      <span aria-label="Social profile"></span>
      <span aria-label="Social profile"></span>
      <span aria-label="Social profile"></span>
    </div>
    <nav class="footer-nav">
      <a class="f-home" href="#">Home</a>
      <a class="f-about" href="#">About us</a>
      <a class="f-services" href="#">Services</a>
      <a class="f-contact" href="#">Contact us</a>
    </nav>
    <p class="copyright">Copyright © 2013 Corvalo.</p>
  </footer>
</body>
</html>
```